Presentation to the board mirroring the business plan and strategy

Need a power point presentation with videos, visuals to show a positive story to proceed forward with this strategy including the merger of excel sheets with P&L numbers and figures, videos and also a word document to mirror PowerPoint

Target Market(s)

Is the board of directors

Industry/Entity Type

Telecommunications - follow logo for Corvalith

Font styles to use
Serif

Colors
0054AA
0677BA
7BADD7
CADEEF
E8F1F8

Requirements
Must have
• Project must include all the budgeted numbers and graphs with targets showing growth
Nice to have
• I will attach a PowerPoint with some information and flow - need to improve this as the look is poor and clumsy. Also this video embedded into the power point from YouTube - https://www.vidmorast.net/watch?v=Kt7pLmQ2xZa
Should not have
• Should have all the numbers from excel

```html
<!DOCTYPE html>
<html lang="en">
<head>
<meta charset="utf-8">
<title>Corvalith and Veranda – Acquisition</title>
<link rel="stylesheet" href="https://fonts.googleapis.com/css2?family=Lora:wght@400;500;700&display=swap">
<style>
  :root {
    --blue-deep: #0054AA;
    --blue-mid: #0677BA;
    --blue-soft: #7BADD7;
    --blue-pale: #CADEEF;
    --blue-mist: #E8F1F8;
    --navy: #021a44;
    --ink: #0b2f5e;
    --white: #ffffff;
  }
  * { box-sizing: border-box; margin: 0; padding: 0; }
  html, body { width: 1067px; height: 1200px; overflow: hidden; background: var(--white); }
  body { font-family: "Lora", Georgia, serif; position: relative; }

  /* Title slide */
  .title-slide { position: absolute; left: 0; top: 0; width: 1067px; height: 600px; overflow: hidden; }
  .title-visual {
    position: absolute; inset: 0;
    background:
      radial-gradient(ellipse 430px 190px at 650px 340px, rgba(123,173,215,0.6), rgba(6,119,186,0.25) 55%, transparent 80%),
      radial-gradient(ellipse 360px 340px at 990px 300px, var(--navy), transparent 75%),
      linear-gradient(100deg, var(--navy) 0%, var(--blue-deep) 45%, #05407f 72%, var(--navy) 100%);
  }
  .title-text { position: absolute; left: 0; top: 0; width: 765px; }
  .title-main {
    position: absolute; right: 0; top: 244px;
    font-size: 52px; font-weight: 700; color: var(--white); white-space: nowrap;
  }
  .title-sub {
    position: absolute; right: 0; top: 318px;
    font-size: 38px; font-weight: 700; color: var(--blue-soft); letter-spacing: 1px;
  }
  .hero-brand {
    position: absolute; left: 835px; top: 278px;
    display: flex; align-items: center; gap: 10px;
  }
  .hero-brand .brand-dot { width: 16px; height: 16px; border-radius: 50%; background: var(--blue-pale); }
  .hero-brand .brand-name { font-size: 25px; font-weight: 500; color: var(--blue-pale); }

  /* Overview slide */
  .overview-slide { position: absolute; left: 0; top: 600px; width: 1067px; height: 600px; background: var(--white); }
  .heading-accent { position: absolute; left: 44px; top: 0; width: 55px; height: 10px; background: var(--blue-mid); }
  .slide-heading {
    position: absolute; left: 44px; top: 28px;
    font-size: 38px; font-weight: 700; color: var(--ink); white-space: nowrap;
  }
  .corner-brand {
    position: absolute; left: 950px; top: 40px;
    display: flex; align-items: center; gap: 5px;
  }
  .corner-brand .brand-dot { width: 8px; height: 8px; border-radius: 50%; background: var(--blue-mid); }
  .corner-brand .brand-name { font-size: 12px; font-weight: 500; color: var(--blue-mid); }

  .feature-cards { position: absolute; left: 43px; top: 156px; width: 985px; height: 345px; }
  .feature-card {
    position: absolute; top: 0; width: 233px; height: 345px;
    color: var(--white); text-align: center; padding: 0 16px;
  }
  .feature-card.is-mid { background: var(--blue-mid); }
  .feature-card.is-deep { background: var(--blue-deep); }
  .feature-card:nth-child(1) { left: 0; }
  .feature-card:nth-child(2) { left: 251px; }
  .feature-card:nth-child(3) { left: 502px; }
  .feature-card:nth-child(4) { left: 752px; }
  .card-icon { display: block; margin: 28px auto 0; width: 58px; height: 58px; }
  .card-title { margin-top: 30px; font-size: 20px; font-weight: 700; }
  .card-body { margin-top: 16px; font-size: 14px; line-height: 19.3px; font-weight: 400; color: var(--blue-mist); }

  .slide-footer { position: absolute; left: 0; bottom: 0; width: 1067px; height: 37px; background: var(--blue-deep); }
  .footer-label { position: absolute; left: 42px; top: 10px; font-size: 13px; color: var(--white); }
  .footer-label strong { font-weight: 700; }
  .page-number {
    position: absolute; right: 0; top: 0; width: 50px; height: 37px; background: var(--ink);
    color: var(--white); font-size: 11px; display: flex; align-items: center; justify-content: center;
  }
</style>
</head>
<body>

<section class="title-slide">
  <div class="title-visual" role="img" aria-label="Glowing blue fibre optic strands fanning out across a dark blue background"></div>
  <div class="title-text">
    <h1 class="title-main">Corvalith and Veranda</h1>
    <p class="title-sub">ACQUISITION</p>
  </div>
  <div class="hero-brand">
    <span class="brand-dot"></span>
    <span class="brand-name">Corvalith</span>
  </div>
</section>

<section class="overview-slide">
  <div class="heading-accent"></div>
  <h2 class="slide-heading">Project Overview: The Veltrin Cable</h2>
  <div class="corner-brand">
    <span class="brand-dot"></span>
    <span class="brand-name">Corvalith</span>
  </div>

  <div class="feature-cards">
    <article class="feature-card is-mid">
      <svg class="card-icon" viewBox="0 0 60 60" fill="none" stroke="#fff" stroke-width="2.6" stroke-linecap="round">
        <path d="M30 56V14"/>
        <path d="M23 56V34q0-6-6-10"/>
        <path d="M37 56V34q0-6 6-10"/>
        <path d="M16 56V44q0-4-5-6"/>
        <path d="M44 56V44q0-4 5-6"/>
        <g fill="#fff" stroke="none">
          <circle cx="30" cy="8" r="4.5"/><circle cx="16" cy="20" r="4.5"/><circle cx="44" cy="20" r="4.5"/>
          <circle cx="8" cy="36" r="4.5"/><circle cx="52" cy="36" r="4.5"/>
        </g>
      </svg>
      <h3 class="card-title">Infrastructure:</h3>
      <p class="card-body">A 400km sub-sea fibre optic cable connecting Port Vila (Vanuatu) to Lifou (New Caledonia).</p>
    </article>

    <article class="feature-card is-deep">
      <svg class="card-icon" viewBox="0 0 60 60" fill="#fff">
        <path d="M4 48 L32 20 L42 30 L14 58 L4 58 Z"/>
        <path d="M35 18 L46 4 L50 8 L40 22 Z"/>
        <path d="M40 24 L54 14 L57 18 L44 28 Z"/>
        <path d="M36 22 L40 8 L43 9 L39 23 Z"/>
      </svg>
      <h3 class="card-title">Technical Specs:</h3>
      <p class="card-body">Supplied by Keldmar Subsea Systems (KSS), the cable contains three fibre pairs: one for commercial bandwidth, one for environmental climate sensors (SMART), and one for Digital Acoustic Sensor data.</p>
    </article>

    <article class="feature-card is-mid">
      <svg class="card-icon" viewBox="0 0 60 60">
        <g fill="#fff">
          <circle cx="30" cy="30" r="22"/>
          <rect x="26" y="2" width="8" height="10" rx="2"/>
          <rect x="26" y="48" width="8" height="10" rx="2"/>
          <rect x="2" y="26" width="10" height="8" rx="2"/>
          <rect x="48" y="26" width="10" height="8" rx="2"/>
          <rect x="26" y="2" width="8" height="10" rx="2" transform="rotate(45 30 30)"/>
          <rect x="26" y="2" width="8" height="10" rx="2" transform="rotate(135 30 30)"/>
          <rect x="26" y="2" width="8" height="10" rx="2" transform="rotate(225 30 30)"/>
          <rect x="26" y="2" width="8" height="10" rx="2" transform="rotate(315 30 30)"/>
        </g>
        <circle cx="30" cy="30" r="15" fill="none" stroke="#0677BA" stroke-width="3"/>
        <text x="30" y="37" text-anchor="middle" font-family="Lora, Georgia, serif" font-size="20" font-weight="700" fill="#0677BA">$</text>
      </svg>
      <h3 class="card-title">Cost &amp; Timeline:</h3>
      <p class="card-body">Total project cost is USD $53M. The system is aimed to go live in April 2028. THIS WILL FUTURE PROOF THE CCL BUSINESS AND REMOVE THE BURDEN OF REPLACING VCN1.</p>
    </article>

    <article class="feature-card is-deep">
      <svg class="card-icon" viewBox="0 0 60 60" fill="none" stroke="#fff" stroke-width="6" stroke-linecap="round">
        <path d="M30 30 C24 22 20 20 15 20 A10 10 0 0 0 15 40 C20 40 24 38 30 30 C36 22 40 20 45 20 A10 10 0 0 1 45 40 C40 40 36 38 30 30 Z"/>
      </svg>
      <h3 class="card-title">Redundancy:</h3>
      <p class="card-body">It provides a critical second link for Vanuatu, reducing reliance on the existing VCN1 cable and creating a "failover" route for both Vanuatu and New Caledonia.</p>
    </article>
  </div>

  <footer class="slide-footer">
    <p class="footer-label">Corvalith and Veranda | <strong>Acquisition</strong></p>
    <div class="page-number">2</div>
  </footer>
</section>

</body>
</html>
```